Bright Paddock Program with the aim of promoting a skills football to school aged children to

Need an A5 back to front one page brochure which is colourful, fun and active to attract the students to purchase the football with part of the funds going back to the school.
Whole idea is to get more footballs in the hands of children of primary school age, fo the school to earn funds from the sale as well as us also making some funds from the sale.
Target Market(s)
5-11 Year old boys and girls
Industry/Entity Type
School
Colors
219ed3
ffffff
0255a3
33b8a4
ec1f27
Requirements
Must have
- Must have football, price, promotional words as per example and contact details of who is ordering the footballs.
- Have included a version we have done up but are not happy with, needs to be much more professional than the attachment to the brief.
Nice to have
- Promotional component on the front with plenty of colours and attraction, with detail requirements on the back
Should not have
- No soccer or KWT balls, only Aussie Rules Footballs in design

```html
<!DOCTYPE html>
<html lang="en">
<head>
<meta charset="utf-8">
<title>Bright Paddock Program – Football for School Flyer</title>
<link rel="stylesheet" href="https://fonts.googleapis.com/css2?family=Bebas+Neue&family=Fjalla+One&family=Open+Sans:wght@600;700&family=Roboto+Condensed:wght@400;700&display=swap">
<style>
  :root {
    --bg: #f2f2f4;
    --grass-light: #3f9a45;
    --grass-dark: #1d6a2e;
    --pitch-dark: #121b15;
    --accent-green: #3cb54a;
    --white: #ffffff;
    --off-white: #e9ece9;
    --form-green: #1f8a3a;
  }
  * { margin: 0; padding: 0; box-sizing: border-box; }
  html, body { width: 1200px; height: 900px; overflow: hidden; background: var(--bg); }
  .canvas { position: relative; width: 1200px; height: 900px; }
  .flyer {
    position: absolute; top: 88px; width: 512px; height: 724px; overflow: hidden;
    background: linear-gradient(160deg, var(--grass-light), var(--grass-dark));
    box-shadow: 0 2px 6px rgba(0,0,0,.25);
  }
  .flyer--front { left: 74px; }
  .flyer--back { left: 614px; }
  .flyer__art { position: absolute; inset: 0; width: 512px; height: 724px; }
  .headline {
    position: absolute; font-family: "Bebas Neue", sans-serif; color: var(--white);
    line-height: 1; text-shadow: 0 3px 6px rgba(0,0,0,.35); white-space: nowrap;
  }
  .headline--main { left: 86px; top: 38px; font-size: 136px; letter-spacing: 1px; }
  .headline--sub { right: 22px; top: 152px; font-size: 88px; letter-spacing: 1px; }
  .promo-box {
    position: absolute; left: 198px; top: 232px; width: 330px; height: 100px;
    border-radius: 12px 0 0 12px; padding: 10px 16px;
    background: linear-gradient(90deg, rgba(10,16,12,.92) 70%, rgba(10,16,12,0));
    font-family: "Fjalla One", sans-serif; font-size: 22px; line-height: 26px; color: var(--white);
  }
  .price { position: absolute; left: 250px; top: 420px; width: 212px; height: 156px; }
  .price text, .callout text { font-family: "Bebas Neue", sans-serif; }
  .price__label { paint-order: stroke; stroke: var(--white); stroke-width: 3px; }
  .order-form {
    position: absolute; left: 40px; top: 582px; width: 432px; height: 106px;
    background: var(--white); border: 3px solid var(--form-green); padding: 8px 12px;
    font-family: "Roboto Condensed", sans-serif; font-size: 7px; color: var(--form-green);
  }
  .order-form__title { font-weight: 700; font-size: 9px; margin-bottom: 9px; }
  .order-form__row { display: flex; align-items: flex-end; gap: 4px; margin-bottom: 9px; }
  .order-form__line { flex: 1; border-bottom: 1px solid var(--form-green); height: 7px; }
  .order-form__check { display: inline-block; width: 10px; height: 10px; border: 1px solid var(--pitch-dark); margin: 0 3px 0 14px; vertical-align: middle; }
  .order-form__row--office { margin-bottom: 4px; }
  .footnote {
    position: absolute; left: 54px; top: 694px; font-family: "Roboto Condensed", sans-serif;
    font-weight: 700; font-size: 7px; color: var(--white);
  }
  .council-name {
    position: absolute; left: 150px; right: 10px; top: 40px; text-align: center;
    font-family: "Open Sans", sans-serif; font-weight: 700; font-size: 22px; line-height: 30px;
    color: var(--white); letter-spacing: 1px;
  }
  .council-name__dot { display: block; width: 46px; height: 46px; margin: 0 auto 14px; border-radius: 50%; background: var(--white); }
  .pitch-copy {
    position: absolute; left: 168px; top: 210px; width: 326px; text-align: center;
    font-family: "Open Sans", sans-serif; font-weight: 600; font-size: 13.6px; line-height: 17.6px; color: var(--white);
  }
  .callout { position: absolute; left: 236px; top: 432px; width: 236px; height: 160px; }
</style>
</head>
<body>
<main class="canvas">

  <section class="flyer flyer--front" aria-label="Front of flyer">
    <svg class="flyer__art" viewBox="0 0 512 724">
      <defs>
        <radialGradient id="ballShade" cx="0.45" cy="0.5" r="0.6">
          <stop offset="0" stop-color="#f48ca4"/>
          <stop offset="0.55" stop-color="#ea3b55"/>
          <stop offset="1" stop-color="#c4142a"/>
        </radialGradient>
        <linearGradient id="edgeGlow" x1="0" x2="1">
          <stop offset="0" stop-color="#3cb54a" stop-opacity="0"/>
          <stop offset="1" stop-color="#7ee07c"/>
        </linearGradient>
      </defs>
      <path d="M0 470 Q260 420 512 300 L512 724 L0 724 Z" fill="var(--pitch-dark)"/>
      <path d="M230 436 Q380 390 512 300 L512 312 Q380 404 230 440 Z" fill="url(#edgeGlow)"/>
      <ellipse role="img" aria-label="Photo of a red leather Aussie Rules football with white laces" cx="-40" cy="610" rx="262" ry="530" fill="url(#ballShade)"/>
    </svg>
    <div class="headline headline--main">FOOTBALL</div>
    <div class="headline headline--sub">FOR SCHOOL</div>
    <div class="promo-box">Order your own exclusive* 12”<br>Skill Football in your local<br>SPFC club colours</div>
    <svg class="price" viewBox="0 0 212 156" aria-label="$70 just each">
      <defs>
        <clipPath id="priceBand"><rect x="0" y="70" width="212" height="62"/></clipPath>
      </defs>
      <text x="0" y="152" font-size="214" textLength="212" lengthAdjust="spacingAndGlyphs" fill="var(--white)">$70</text>
      <g clip-path="url(#priceBand)">
        <text x="0" y="152" font-size="214" textLength="212" lengthAdjust="spacingAndGlyphs" fill="var(--accent-green)">$70</text>
      </g>
      <text class="price__label" x="18" y="124" font-size="60" textLength="180" lengthAdjust="spacingAndGlyphs" fill="var(--pitch-dark)">JUST EACH</text>
    </svg>
    <form class="order-form">
      <div class="order-form__title">ORDER INFORMATION</div>
      <div class="order-form__row">Student Name: <span class="order-form__line"></span></div>
      <div class="order-form__row">Year: <span class="order-form__line" style="flex:.3"></span> Classroom: <span class="order-form__line"></span> Number of footballs: <span class="order-form__line" style="flex:.25"></span></div>
      <div class="order-form__row">Payment method: <span class="order-form__check"></span>Cash <span class="order-form__check"></span>Cheque <span class="order-form__check"></span>EFT</div>
      <div class="order-form__row order-form__row--office">OFFICE ONLY</div>
      <div class="order-form__row">Payment received: <span class="order-form__line" style="flex:.4"></span><span style="flex:.6"></span></div>
    </form>
    <p class="footnote">*Offer only available at selected schools</p>
  </section>

  <section class="flyer flyer--back" aria-label="Back of flyer">
    <svg class="flyer__art" viewBox="0 0 512 724">
      <defs>
        <radialGradient id="ballShadeBack" cx="0.45" cy="0.5" r="0.6">
          <stop offset="0" stop-color="#f48ca4"/>
          <stop offset="0.55" stop-color="#ea3b55"/>
          <stop offset="1" stop-color="#c4142a"/>
        </radialGradient>
        <linearGradient id="edgeGlowBack" x1="0" x2="1">
          <stop offset="0" stop-color="#3cb54a" stop-opacity="0"/>
          <stop offset="1" stop-color="#7ee07c"/>
        </linearGradient>
      </defs>
      <path d="M0 470 Q260 420 512 300 L512 724 L0 724 Z" fill="var(--pitch-dark)"/>
      <path d="M230 436 Q380 390 512 300 L512 312 Q380 404 230 440 Z" fill="url(#edgeGlowBack)"/>
      <ellipse role="img" aria-label="Photo of a red leather Aussie Rules football with white laces" cx="-40" cy="610" rx="262" ry="530" fill="url(#ballShadeBack)"/>
    </svg>
    <div class="council-name"><span class="council-name__dot"></span>SOUTHERN PLAINS<br>FOOTY COUNCIL INC.</div>
    <p class="pitch-copy">and improve your technique this season and help fundraise money for your school. All orders delivered in Term 2 just in time for footy season. $5 from each football purchased will go straight back to your schools P&amp;C!</p>
    <svg class="callout" viewBox="0 0 236 160" aria-label="Don’t miss out on a footy!">
      <text x="0" y="34" font-size="42" textLength="232" lengthAdjust="spacingAndGlyphs" fill="var(--white)">DON’T MISS OUT ON A</text>
      <text x="0" y="148" font-size="122" textLength="232" lengthAdjust="spacingAndGlyphs" fill="var(--off-white)">FOOTY!</text>
    </svg>
    <form class="order-form">
      <div class="order-form__title">ORDER INFORMATION</div>
      <div class="order-form__row">Student Name: <span class="order-form__line"></span></div>
      <div class="order-form__row">Year: <span class="order-form__line" style="flex:.3"></span> Classroom: <span class="order-form__line"></span> Number of footballs: <span class="order-form__line" style="flex:.25"></span></div>
      <div class="order-form__row">Payment method: <span class="order-form__check"></span>Cash <span class="order-form__check"></span>Cheque <span class="order-form__check"></span>EFT</div>
      <div class="order-form__row order-form__row--office">OFFICE ONLY</div>
      <div class="order-form__row">Payment received: <span class="order-form__line" style="flex:.4"></span><span style="flex:.6"></span></div>
    </form>
    <p class="footnote">*Offer only available at selected schools</p>
  </section>

</main>
</body>
</html>
```